Brindle construction ltd staionary design
Project: Stationary
Stationary - Construction
Stationary
Professional
Directors Dan Brindle / Mark Brindle
BRINDLE CONSTRUCTION (GLOUCESTER) LTD
14 wexcombe road Gloucester GL4 8RQ
Brindleconstructionltd@fernmail.example
www.brindleconstructionlimited.example
would like stationary pack designed: business card, letterhead, envelope ect. Also a site sign please. Business card i would like black background to contrast my green logo with the logo in middle and details underneath. Letterhead i will leave to designer to come up with options. On site sign can i have logo ontop as main feature and underneath contact info with services incl ( New Builds, Extensions, Conversions, Refurbishments, Groundworks, Block Paving.) In logo attached use main logo ontop.
Main logo and underneath building contractor & Block paving specialist

```html
<!DOCTYPE html>
<html lang="en">
<head>
<meta charset="utf-8">
<title>Brindle Construction Ltd – Business Card</title>
<link href="https://fonts.googleapis.com/css2?family=Arimo:wght@400;700&family=Michroma&display=swap" rel="stylesheet">
<style>
  :root {
    --page-bg: #e9e7e3;
    --card-black: #0c0c0c;
    --card-black-soft: #1c1c1c;
    --brand-green: #3fae3a;
    --green-light: #3caa36;
    --green-dark: #17601a;
    --swoosh-grey: #8d8d8d;
    --text-white: #ffffff;
    --text-soft: #e6f3e4;
  }
  * { margin: 0; padding: 0; box-sizing: border-box; }
  html, body {
    width: 1200px; height: 780px; overflow: hidden;
    background: var(--page-bg);
  }
  .canvas { position: relative; width: 1200px; height: 780px; }
  .business-card {
    position: absolute; left: 100px; top: 90px;
    width: 1000px; height: 600px;
    border-radius: 34px; overflow: hidden;
    background: linear-gradient(180deg, var(--card-black-soft), var(--card-black) 55%);
    box-shadow: 0 18px 40px rgba(0,0,0,0.25);
  }
  .card-wave { position: absolute; inset: 0; width: 1000px; height: 600px; }
  .brand-name {
    position: absolute; left: 0; right: 0; top: 78px;
    text-align: center;
    font-family: "Michroma", sans-serif;
    font-size: 54px; line-height: 1.25; letter-spacing: 3px;
    color: var(--brand-green);
    text-transform: uppercase;
  }
  .brand-name .brand-sub { display: block; font-size: 30px; letter-spacing: 4px; }
  .contact-person {
    position: absolute; left: 150px; top: 392px;
    font-family: "Arimo", sans-serif; color: var(--text-white);
  }
  .contact-person .person-name { font-size: 30px; font-weight: 700; }
  .contact-person .person-phone { font-size: 22px; margin-top: 10px; color: var(--text-soft); }
  .divider {
    position: absolute; left: 420px; top: 345px;
    width: 2px; height: 190px; background: var(--text-white); opacity: 0.85;
  }
  .company-details {
    position: absolute; left: 448px; top: 322px;
    font-family: "Arimo", sans-serif; color: var(--text-white);
    font-size: 20px; line-height: 1.35;
  }
  .address { margin-bottom: 26px; }
  .detail-row { display: flex; align-items: center; gap: 12px; height: 30px; }
  .detail-row svg { width: 20px; height: 20px; flex: none; }
</style>
</head>
<body>
<main class="canvas">
  <section class="business-card" aria-label="Brindle Construction Ltd business card">
    <svg class="card-wave" viewBox="0 0 1000 600" aria-hidden="true">
      <defs>
        <linearGradient id="greenFill" x1="0" y1="0" x2="0" y2="1">
          <stop offset="0" stop-color="var(--green-light)"/>
          <stop offset="1" stop-color="var(--green-dark)"/>
        </linearGradient>
        <linearGradient id="greySwoosh" x1="0" y1="0" x2="1" y2="0">
          <stop offset="0" stop-color="#555"/>
          <stop offset="0.5" stop-color="var(--swoosh-grey)"/>
          <stop offset="1" stop-color="#cfcfcf"/>
        </linearGradient>
      </defs>
      <path d="M0,290 C260,300 520,290 1000,120 L1000,180 C600,300 300,320 0,330 Z" fill="url(#greySwoosh)"/>
      <path d="M0,320 C300,318 620,290 1000,170 L1000,600 L0,600 Z" fill="url(#greenFill)"/>
    </svg>

    <h1 class="brand-name">Brindle<span class="brand-sub">construction ltd</span></h1>

    <div class="contact-person">
      <p class="person-name">Mark Brindle</p>
      <p class="person-phone">07700 900456</p>
    </div>

    <div class="divider"></div>

    <div class="company-details">
      <p class="address">14 wexcombe road,<br>Gloucester, GL4 8RQ</p>
      <p class="detail-row">
        <svg viewBox="0 0 20 20" aria-hidden="true"><path d="M5 2h3l1 4-2 1.5a10 10 0 0 0 5.5 5.5L14 11l4 1v3a2 2 0 0 1-2 2C8.8 17 3 11.2 3 4a2 2 0 0 1 2-2z" fill="#fff"/></svg>
        01452 000123
      </p>
      <p class="detail-row">
        <svg viewBox="0 0 20 20" aria-hidden="true"><rect x="5" y="1" width="10" height="18" rx="2" fill="#fff"/><rect x="7" y="4" width="6" height="9" fill="#2c8a2a"/><circle cx="10" cy="16" r="1.2" fill="#2c8a2a"/></svg>
        07700 900456
      </p>
      <p class="detail-row">
        <svg viewBox="0 0 20 20" aria-hidden="true"><rect x="1" y="4" width="18" height="12" rx="1.5" fill="#fff"/><path d="M2 5l8 6 8-6" stroke="#2c8a2a" stroke-width="1.6" fill="none"/></svg>
        Brindleconstructionltd@fernmail.example
      </p>
    </div>
  </section>
</main>
</body>
</html>
```